Innovation Presentation Template

I need a unique template design for a presentation on Innovation used exclusively inside of our company. I'd prefer to work in Apple Keynote but can take a .ppt and convert it. The template should appeal to a broad audience of diverse job descriptions. This is a one-time presentation that will last between 30 and 45 minutes. The design should provide a strong visual appeal with multiple chart layouts to support highlighted test points (no bullets, I hate bullets), graphics, line art, and video/photos. My presentations are sparse, never more that 2 concepts per chart (usually one). Our company is a high tech manufacturer selling products in many markets ranging from Government to consumer. The final design should include style a style guide including suggested fonts, colors, graph formats, suggested word art, etc.

Target Market(s)

The audience is internal employees only. Strong corporate branding is not required in this presentation.

Industry/Entity Type

Government

Colors
3277b5
faa54b

Requirements
Must have
• Strong visual appeal helping to support the communication of simple concepts (that have been broken down from complex subject matter).

Multiple chart template forms to support different forms of communication including text points, data charts, graphics, photos, and videos.

Visuals will be memorable, but not overpower the content. Visuals will help convey the content.

Well conceived and coordinated color pallets. Fonts guides (that I can access).

You can visit our company web site at www.KOVEX.com to see logo and corporate look/feel. It would be good to build logo into a few of the chart templates, but not all.
Nice to have
• Keynote (please). I can live with .ppt if I have to.

Many charts will make a point with simple single sentences. Find a way to make the sentences graphically interesting by varying font and/or color of specific words to help drive points.

Note that colors that I've identified below are based upon the blue used in our logo and the orange that complements it. I'm not married to these but use them as guidelines.
Should not have
• Noise. Corporate nauseia.

```html
<!DOCTYPE html>
<html lang="en">
<head>
<meta charset="utf-8">
<title>Project Title Here</title>
<link href="https://fonts.googleapis.com/css2?family=Saira+Semi+Condensed:wght@300;400;600;700;800&display=swap" rel="stylesheet">
<style>
  :root {
    --header-deep: #1f63c0;
    --header-mid: #2f8ae0;
    --header-light: #7cc4f2;
    --accent-yellow: #ffd400;
    --heading-blue: #0f4c9a;
    --brand-blue: #1b55a3;
    --body-text: #3a3a3a;
    --page-bg: #f5f7f8;
    --footer-text: #1a1a1a;
    --white: #ffffff;
  }
  * { margin: 0; padding: 0; box-sizing: border-box; }
  html, body { width: 1200px; height: 900px; overflow: hidden; }
  body {
    font-family: "Saira Semi Condensed", "Arial Narrow", sans-serif;
    background: var(--page-bg);
    position: relative;
  }
  .slide-header {
    position: absolute; left: 0; top: 0; width: 1200px; height: 126px;
    background: linear-gradient(90deg, var(--header-deep) 0%, var(--header-mid) 50%, var(--header-light) 85%, #a9def7 100%);
  }
  .header-rule {
    position: absolute; left: 0; top: 126px; width: 1200px; height: 7px;
    background: var(--accent-yellow);
    border-top: 2px solid var(--white);
  }
  .slide-title {
    position: absolute; left: 49px; top: 22px;
    font-weight: 300; font-size: 62px; line-height: 80px;
    color: var(--white); letter-spacing: 1px;
  }
  .brand-name {
    position: absolute; right: 24px; top: 22px;
    font-weight: 800; font-size: 74px; line-height: 80px;
    color: var(--brand-blue); letter-spacing: 1px;
  }
  .column { position: absolute; top: 240px; width: 496px; }
  .column-left { left: 52px; }
  .column-right { left: 645px; }
  .column-heading {
    font-weight: 700; font-size: 34px; line-height: 48px;
    color: var(--heading-blue); margin-bottom: 12px;
  }
  .column-text {
    font-size: 20px; line-height: 36px; color: var(--body-text);
    text-align: justify; margin-bottom: 36px;
  }
  .slide-footer {
    position: absolute; left: 0; top: 852px; width: 1200px; height: 48px;
    background: var(--accent-yellow);
    border-top: 2px solid #e8e8e8;
  }
  .copyright {
    position: absolute; left: 16px; top: 10px;
    font-size: 19px; line-height: 28px; color: var(--footer-text); font-weight: 500;
  }
  .page-marker { position: absolute; left: 1075px; top: 837px; width: 72px; height: 63px; }
  .page-number {
    position: absolute; left: 1075px; top: 856px; width: 72px;
    text-align: center; font-weight: 700; font-size: 30px; line-height: 44px; color: var(--white);
  }
</style>
</head>
<body>
  <header class="slide-header">
    <h1 class="slide-title">PROJECT TITLE HERE</h1>
    <div class="brand-name">KOVEX</div>
  </header>
  <div class="header-rule"></div>

  <section class="column column-left">
    <h2 class="column-heading">Lorem ipsum dolor sit ipsum</h2>
    <p class="column-text">Lorem ipsum dolor sit ipsum Lorem ipsum dolor sit ipsum Lorem ipsum dolor sit ipsum Lorem ipsum dolor sit ipsum lorem ipsum dolor sit ipsum Lorem ipsum dolor sit ipsum Lorem ipsum dolor sit ipsum</p>
    <p class="column-text">Lorem ipsum dolor sit ipsum Lorem ipsum dolor sit ipsum Lorem ipsum dolor sit ipsum Lorem ipsum dolor sit ipsum lorem ipsum dolor sit ipsum Lorem ipsum dolor sit ipsum Lorem ipsum dolor sit ipsum Lorem ipsum dolor sit ipsum</p>
  </section>

  <section class="column column-right">
    <h2 class="column-heading">Lorem ipsum dolor sit ipsum</h2>
    <p class="column-text">Lorem ipsum dolor sit ipsum Lorem ipsum dolor sit ipsum Lorem ipsum dolor sit ipsum Lorem ipsum dolor sit ipsum lorem ipsum dolor sit ipsum Lorem ipsum dolor sit ipsum Lorem ipsum dolor sit ipsum</p>
    <p class="column-text">Lorem ipsum dolor sit ipsum Lorem ipsum dolor sit ipsum Lorem ipsum dolor sit ipsum Lorem ipsum dolor sit ipsum lorem ipsum dolor sit ipsum Lorem ipsum dolor sit ipsum Lorem ipsum dolor sit ipsum Lorem ipsum dolor sit ipsum</p>
  </section>

  <footer class="slide-footer">
    <span class="copyright">Copyright text here</span>
  </footer>
  <svg class="page-marker" viewBox="0 0 72 63" aria-hidden="true">
    <polygon points="36,0 72,27 72,63 0,63 0,27" fill="#0f4c9a"/>
  </svg>
  <div class="page-number">1</div>
</body>
</html>
```